Create a professional, eye-catching business card design that reflects the values and services of Brookfern Veterinary Hospital. we provide veterinary services and the business card should be a memorable representation of the clinic and align with its branding and mission. our tag line is "Faithful Friends, Gentle Care for Life"
Use clean, modern typography. Prioritize readability and professionalism. We would like to see designs that use the color blue, as in the logo example. the final design should communicate professionalism and care, with attention to detail.

```html
<!DOCTYPE html>
<html lang="en">
<head>
<meta charset="UTF-8">
<title>Brookfern Veterinary Hospital — Business Card</title>
<link href="https://fonts.googleapis.com/css2?family=Montserrat:wght@400;500;700;800&display=swap" rel="stylesheet">
<style>
  :root {
    --navy: #0c2461;
    --brand-blue: #1b78c6;
    --white: #ffffff;
    --backdrop: #2f2f31;
    --card-radius: 34px;
  }
  * { margin: 0; padding: 0; box-sizing: border-box; }
  html, body {
    width: 1200px; height: 1200px; overflow: hidden;
    background: var(--backdrop);
    font-family: "Montserrat", sans-serif;
  }
  .canvas {
    width: 1200px; height: 1200px;
    display: flex; flex-direction: column; align-items: center; justify-content: center;
    gap: 60px;
  }
  .card {
    position: relative;
    width: 780px; height: 446px;
    border-radius: var(--card-radius);
    overflow: hidden;
    box-shadow: 0 18px 40px rgba(0,0,0,0.45);
  }

  /* Front */
  .card--front { background: var(--navy); }
  .card--front .panel-shape { position: absolute; inset: 0; width: 100%; height: 100%; }
  .brand {
    position: absolute;
    display: flex; align-items: center; gap: 14px;
    font-weight: 800; letter-spacing: 0.5px; line-height: 1.05;
  }
  .brand__mark {
    flex: none; width: 52px; height: 52px; border-radius: 50%;
    border: 3px solid currentColor;
  }
  .brand__name { font-size: 28px; text-transform: uppercase; }
  .brand__name small { display: block; font-size: 13px; letter-spacing: 1.4px; margin-top: 6px; }
  .card--front .brand { left: 40px; top: 196px; color: var(--navy); }

  .contact-block {
    position: absolute; left: 430px; top: 92px; color: var(--white);
  }
  .person__name { font-size: 46px; font-weight: 500; color: var(--brand-blue); line-height: 1; letter-spacing: -0.5px; }
  .person__role { font-size: 22px; font-weight: 400; margin-top: 4px; letter-spacing: 0.5px; }
  .contact-list { list-style: none; margin-top: 26px; }
  .contact-list li {
    display: flex; align-items: center; gap: 14px;
    font-size: 21px; font-weight: 400; height: 34px;
  }
  .contact-list svg { width: 22px; height: 22px; flex: none; fill: none; stroke: var(--brand-blue); stroke-width: 2; }

  /* Back */
  .card--back { background: var(--navy); color: var(--white); }
  .card--back .brand { left: 50%; top: 130px; transform: translateX(-50%); color: var(--white); }
  .card--back .brand__mark { width: 74px; height: 74px; }
  .card--back .brand__name { font-size: 40px; }
  .card--back .brand__name small { font-size: 19px; }
  .tagline {
    position: absolute; left: 0; right: 0; top: 312px;
    text-align: center; font-size: 27px; font-weight: 700; letter-spacing: 0.5px;
  }
</style>
</head>
<body>
<main class="canvas">

  <section class="card card--front" aria-label="Business card front">
    <svg class="panel-shape" viewBox="0 0 780 446" preserveAspectRatio="none" aria-hidden="true">
      <path d="M0 0 H250 C330 90 380 250 395 446 H0 Z" fill="#ffffff"/>
      <path d="M250 0 C330 90 380 250 395 446" fill="none" stroke="#1b78c6" stroke-width="9"/>
    </svg>

    <div class="brand">
      <span class="brand__mark"></span>
      <span class="brand__name">Brookfern<small>Veterinary Hospital</small></span>
    </div>

    <div class="contact-block">
      <p class="person__name">FULL NAME</p>
      <p class="person__role">POSITION</p>
      <ul class="contact-list">
        <li>
          <svg viewBox="0 0 24 24"><path d="M5 3h4l2 5-2.5 1.5a11 11 0 0 0 6 6L16 13l5 2v4a2 2 0 0 1-2 2A17 17 0 0 1 3 5a2 2 0 0 1 2-2z"/></svg>
          (000) 000 0000
        </li>
        <li>
          <svg viewBox="0 0 24 24"><rect x="7" y="2" width="10" height="20" rx="2"/><path d="M11 18h2"/></svg>
          (000) 000 0000
        </li>
        <li>
          <svg viewBox="0 0 24 24"><rect x="3" y="5" width="18" height="14" rx="1"/><path d="M3 6l9 7 9-7"/></svg>
          email@company.com
        </li>
        <li>
          <svg viewBox="0 0 24 24"><circle cx="12" cy="12" r="9"/><path d="M3 12h18M12 3c3 3 3 15 0 18M12 3c-3 3-3 15 0 18"/></svg>
          www.company.com
        </li>
      </ul>
    </div>
  </section>

  <section class="card card--back" aria-label="Business card back">
    <div class="brand">
      <span class="brand__mark"></span>
      <span class="brand__name">Brookfern<small>Veterinary Hospital</small></span>
    </div>
    <p class="tagline">Faithful Friends, Gentle Care for Life</p>
  </section>

</main>
</body>
</html>
```